Dietitian/Nutritionist seeks trifold marketing brochure

We need a trifold brochure for marketing to patients within a doctors surgery. This will be a source of information for prospective patients, what they can expect and how to contact us. The brochure needs to have some key information such as a brief description of the services available, fees, locations of clinics and contact information. Our current brochure has been uploaded which has the information you need to complete this project. The files you provide will allow us to edit the information at a later date as pricing and services change.

Target Market(s)

Patients who have been referred to see a dietitian/nutritionist and people who are considering seeing a dietitian/nutritionist but haven't decided

Industry/Entity Type

Dietician

Font styles to use
Serif

Colors

Designer to choose colors to be used in the design.

Requirements
Must have
• My logo
• Verified clinical mealwise logo
• My website address and contact details
• Most of the information that is in my current brochure
• Locations/names of the four clinics
Nice to have
• Images that promote cooking, health and wellbeing

```html
<!DOCTYPE html>
<html lang="en">
<head>
<meta charset="utf-8">
<title>Harbourline Nutrition &amp; Dietetics – Trifold Brochure</title>
<link rel="stylesheet" href="https://fonts.googleapis.com/css2?family=Courier+Prime:wght@400;700&display=swap">
<style>
  :root {
    --page-bg: #d9d9d9;
    --paper: #ffffff;
    --paper-grey: #ececec;
    --brand-green: #6cb33f;
    --brand-green-text: #4f9a2a;
    --brand-blue: #1d4fa0;
    --badge-orange: #ef6a2e;
    --dot-tone: #e4ebf0;
    --map-tone: #cfd4d8;
    --photo-tone: #efe6dc;
    --text-grey: #5d6a60;
    --white: #ffffff;
  }
  * { box-sizing: border-box; margin: 0; padding: 0; }
  html, body { width: 1055px; height: 1200px; overflow: hidden; }
  body {
    background: var(--page-bg);
    font-family: "Courier Prime", serif;
    display: flex; align-items: center; justify-content: center;
  }
  .brochure {
    display: flex;
    width: 990px; height: 720px;
    box-shadow: 0 10px 30px rgba(0,0,0,.18);
  }
  .panel { position: relative; width: 330px; height: 100%; overflow: hidden; }

  /* Cover panel */
  .panel--cover { background: var(--paper); }
  .cover-pattern {
    position: absolute; inset: 0;
    background: linear-gradient(180deg, var(--dot-tone), #f3f6f8);
    opacity: .6;
  }
  .brand {
    position: absolute; left: 40px; top: 300px;
    display: flex; align-items: center; gap: 12px;
  }
  .brand-dot { width: 42px; height: 42px; border-radius: 50%; background: var(--brand-blue); flex: none; }
  .brand-name {
    color: var(--brand-blue); font-weight: 700; font-size: 18px; line-height: 1.25;
  }
  .website {
    position: absolute; left: 30px; right: 30px; bottom: 48px;
    border: 1.5px solid var(--brand-green); border-radius: 14px;
    padding: 4px 8px; text-align: center;
    color: var(--brand-green-text); font-size: 12px;
  }

  /* Middle panel */
  .panel--intro { background: var(--paper); }
  .food-photo {
    position: absolute; left: 45px; top: 25px; width: 240px; height: 230px;
    border-radius: 50%;
    background: radial-gradient(circle, #f6c77a 0%, var(--photo-tone) 55%, var(--paper) 75%);
  }
  .intro-band { position: absolute; left: 0; top: 270px; width: 100%; height: 450px; }
  .intro-copy {
    position: absolute; left: 28px; right: 28px; top: 330px;
    color: var(--white); font-size: 14px; line-height: 1.5; text-align: center;
  }
  .intro-copy p + p { margin-top: 22px; }
  .accreditation {
    position: absolute; right: 22px; bottom: 40px;
    width: 150px; height: 96px; background: var(--badge-orange);
    display: flex; align-items: center; justify-content: space-between;
    padding: 10px; color: var(--white); font-size: 12px; line-height: 1.25;
  }
  .accreditation-mark { width: 44px; height: 44px; border-radius: 50%; background: var(--white); flex: none; }

  /* Contact panel */
  .panel--contact { background: var(--paper-grey); }
  .world-map {
    position: absolute; left: 10px; top: 20px; width: 310px; height: 200px;
    background: radial-gradient(ellipse at center, var(--map-tone), var(--paper-grey) 70%);
  }
  .contact {
    position: absolute; left: 20px; right: 20px; top: 280px;
    text-align: center; color: var(--brand-green-text);
  }
  .contact-name { font-weight: 700; font-size: 16px; letter-spacing: 2px; line-height: 1.3; }
  .contact-phone { font-weight: 700; font-size: 16px; letter-spacing: 1px; margin-top: 4px; }
  .contact-email { font-size: 11px; margin-top: 12px; }
  .contact-hours { font-size: 11px; margin-top: 10px; }
  .contact-role { font-weight: 700; font-size: 11px; margin-top: 2px; }

  .practice-info {
    position: absolute; left: 28px; right: 28px; top: 460px;
    text-align: center; color: var(--text-grey);
    font-size: 11px; line-height: 1.4;
  }
  .info-heading {
    color: var(--brand-green-text); font-weight: 700; font-size: 12px;
    letter-spacing: 1px; text-transform: uppercase;
  }
  .info-block + .info-block { margin-top: 12px; }
  .clinic-list { list-style: none; }
</style>
</head>
<body>
  <main class="brochure">
    <section class="panel panel--cover">
      <div class="cover-pattern" role="img" aria-label="Soft dotted grid background pattern"></div>
      <div class="brand">
        <span class="brand-dot"></span>
        <span class="brand-name">Harbourline<br>Nutrition &amp; Dietetics</span>
      </div>
      <div class="website">www.harbourlinenutrition.com.au</div>
    </section>

    <section class="panel panel--intro">
      <div class="food-photo" role="img" aria-label="Photo of a healthy breakfast plate with fruit and pastries seen from above"></div>
      <svg class="intro-band" viewBox="0 0 330 450" preserveAspectRatio="none" aria-hidden="true">
        <path d="M0 40 Q165 -10 330 20 L330 450 L0 450 Z" fill="var(--brand-green)"/>
      </svg>
      <div class="intro-copy">
        <p>Helping you to meet your individual nutrition goals with an emphasis on practical skills, every foods and providing you with up to date advice</p>
        <p>We work together to develop personalised eating plans that take your lifestyle into account.</p>
      </div>
      <div class="accreditation">
        <span>Verified clinical mealwise</span>
        <span class="accreditation-mark"></span>
      </div>
    </section>

    <section class="panel panel--contact">
      <div class="world-map" role="img" aria-label="Dotted world map in light grey"></div>
      <div class="contact">
        <p class="contact-name">DANIEL<br>WHITCOMBE</p>
        <p class="contact-phone">0491570156</p>
        <p class="contact-email">daniel.w.nutrition@mailbox.com</p>
        <p class="contact-hours">Hours: 9am–5pm</p>
        <p class="contact-role">Verified clinical mealwise &amp; Chef</p>
      </div>
      <div class="practice-info">
        <div class="info-block">
          <p class="info-heading">Services</p>
          <p>Weight management · Diabetes · Heart health · Gut health · Cooking skills</p>
        </div>
        <div class="info-block">
          <p class="info-heading">Fees</p>
          <p>Initial consult $120 · Review $75</p>
          <p>Rebates available</p>
        </div>
        <div class="info-block">
          <p class="info-heading">Clinics</p>
          <ul class="clinic-list">
            <li>Harbourline Medical Centre</li>
            <li>Westgate Family Practice</li>
            <li>Riverbend GP Clinic</li>
            <li>Eastbrook Health Hub</li>
          </ul>
        </div>
      </div>
    </section>
  </main>
</body>
</html>
```